Forest Consultant/Timber Buyer needs a clean business card

We are a forestry consulting and timber buying company. We meet with private landowners and assist them with timber management and timber harvesting. We would like a professional business card, please no clip art. logo is blue and white but would like to see a gray,silver, or some other color incorporated. Would like basic contact info. Would like to the layout to be creative and sleek but masculine.

Target Market(s)

private landowners

Industry/Entity Type

Business

Contact Information for Business Card

name,position, cell number, office number, email, website. This might be to cluttered. Basic contact info is what we are looking for.

Contact info can all be on one side with logo on the other.

Font styles to use
Serif
Sans Serif

Colors
0255a3
ffffff
aaaaaa

Requirements
Must have
• We just want it professional.
Nice to have
• Creative layout.
Should not have
• please no clip art of log trucks etc.

```html
<!DOCTYPE html>
<html lang="en">
<head>
<meta charset="utf-8">
<title>Heritage Ridge Forestry – Business Card</title>
<link rel="stylesheet" href="https://fonts.googleapis.com/css2?family=Open+Sans:wght@400;600;700&display=swap">
<style>
  :root{
    --brand-blue:#0255a3;
    --white:#ffffff;
    --silver:#aaaaaa;
    --stage:#2b2b2d;
  }
  html,body{margin:0;padding:0;overflow:hidden;}
  body{
    width:1200px;height:900px;background:var(--stage);
    position:relative;font-family:"Open Sans",sans-serif;
  }
  .card{
    position:absolute;width:560px;height:320px;border-radius:22px;
    overflow:hidden;box-shadow:0 12px 30px rgba(0,0,0,.45);
  }
  /* back side */
  .card-back{left:90px;top:110px;background:var(--brand-blue);}
  .back-brand{
    position:absolute;inset:0;display:flex;align-items:center;justify-content:center;gap:14px;
    color:var(--white);font-weight:700;font-size:30px;letter-spacing:.5px;
  }
  .brand-dot{width:22px;height:22px;border-radius:50%;background:var(--white);}
  /* front side */
  .card-front{left:550px;top:470px;background:var(--brand-blue);}
  .front-shape{position:absolute;inset:0;}
  .side-tab{position:absolute;left:0;top:150px;width:12px;height:46px;background:var(--silver);border-radius:0 6px 6px 0;}
  .person{position:absolute;left:40px;top:92px;color:var(--white);}
  .person-name{font-weight:700;font-size:22px;letter-spacing:1px;margin:0;}
  .person-role{font-size:12px;letter-spacing:1.5px;margin:2px 0 0;text-transform:uppercase;}
  .front-brand{
    position:absolute;right:30px;top:52px;display:flex;align-items:center;gap:10px;
    color:var(--brand-blue);font-weight:700;font-size:22px;letter-spacing:.3px;
  }
  .front-brand .brand-dot{background:var(--brand-blue);width:16px;height:16px;}
  .contacts{position:absolute;right:26px;top:142px;list-style:none;margin:0;padding:0;text-align:right;}
  .contacts li{
    display:flex;justify-content:flex-end;align-items:center;gap:8px;
    color:var(--brand-blue);font-size:13.5px;line-height:21px;
  }
  .contacts svg{width:11px;height:11px;fill:none;stroke:#333;stroke-width:1.6;}
</style>
</head>
<body>
  <section class="card card-back" aria-label="Business card back">
    <div class="back-brand"><span class="brand-dot"></span>Heritage Ridge Forestry</div>
  </section>

  <section class="card card-front" aria-label="Business card front">
    <svg class="front-shape" viewBox="0 0 560 320" preserveAspectRatio="none" aria-hidden="true">
      <rect width="560" height="320" fill="var(--brand-blue)"/>
      <ellipse cx="430" cy="95" rx="230" ry="228" fill="var(--silver)"/>
      <ellipse cx="442" cy="88" rx="226" ry="226" fill="var(--white)"/>
    </svg>
    <span class="side-tab"></span>
    <div class="person">
      <p class="person-name">MARK ELLISON</p>
      <p class="person-role">Director</p>
    </div>
    <div class="front-brand"><span class="brand-dot"></span>Heritage Ridge Forestry</div>
    <ul class="contacts">
      <li>+330 5182-4416
        <svg viewBox="0 0 12 12"><path d="M2 1.5l2 0 1 2.5-1.3 1a6 6 0 0 0 3.3 3.3l1-1.3 2.5 1v2a1 1 0 0 1-1 1A9 9 0 0 1 1 2.5a1 1 0 0 1 1-1z"/></svg></li>
      <li>+330 5127-9053
        <svg viewBox="0 0 12 12"><rect x="3" y="1" width="6" height="10" rx="1"/><path d="M5 9.3h2"/></svg></li>
      <li>info@heritageridgeforestry.com
        <svg viewBox="0 0 12 12"><rect x="1" y="2.5" width="10" height="7" rx="1"/><path d="M1 3l5 3.5L11 3"/></svg></li>
      <li>www.heritageridgeforestry.com
        <svg viewBox="0 0 12 12"><circle cx="6" cy="6" r="5"/><path d="M1 6h10M6 1c2.5 2.8 2.5 7.2 0 10M6 1c-2.5 2.8-2.5 7.2 0 10"/></svg></li>
    </ul>
  </section>
</body>
</html>
```